Presentation Folder for dental clinic

We need a presentation folder design. The presentation folder is what we give to our patients with treatment plans, quotes, images, information sheets etc.
I have uploaded current stationary designs for assistance as well as a photo of our external sign design.
We are an upmarket dental clinic.
Professionalism and customer service is key to us.
We provide information in presentation folders to give to patients.
It needs to memorable and a statement to who we are.

Target Market(s)

Main patient base is Male and Female 40 years old to 70 years old

Industry/Entity Type

Dental Clinic

Font styles to use
Serif
Sans Serif

Requirements
Must have
• Design:
• -Professional
• -Timeless
• -Modern
• - Memorable
• - Statement (if a patient puts down the folder, it will be easily identifiable with as Corvel Dentals folder)
• Logo
• Address, phone, email, website
• Dr Leo Brandt name and degree details
• Colour scheme to match current logos and branding
• "Your Smile Our Passion" quote
Nice to have
• Services listed:
• - Sleep Dentistry
• - Happy Gas
• - Dental Implants
• - Cosmetic Dentistry
• - Oral Surgery
• - Alignora
• - Teeth Whitening
• - General Dentistry
• - Childrens Dentistry
• See website www.corveldental-example.com.au
Should not have
• Dental cliche photos

```html
<!DOCTYPE html>
<html lang="en">
<head>
<meta charset="utf-8">
<title>Corvel Dental – Presentation Folder</title>
<link href="https://fonts.googleapis.com/css2?family=Lato:wght@400;700;900&family=Merriweather:wght@400;700&display=swap" rel="stylesheet">
<style>
  :root{
    --purple:#7a3a93;
    --purple-dark:#5f2a75;
    --grey:#9a9a9f;
    --grey-light:#d9d9dc;
    --ink:#2e2e33;
    --paper:#ffffff;
    --bg:#ecebe8;
    --photo-a:#8d9aa6;
    --photo-b:#4b4f58;
  }
  *{box-sizing:border-box;margin:0;padding:0}
  html,body{width:1200px;height:2486px;overflow:hidden;background:var(--bg)}
  body{position:relative;font-family:"Lato",Arial,sans-serif;color:var(--ink)}
  .panel{position:absolute;left:170px;width:860px;height:1150px;background:var(--paper);box-shadow:0 10px 30px rgba(0,0,0,.12);overflow:hidden}
  .panel--back{top:60px}
  .panel--front{top:1276px}
  .shapes{position:absolute;inset:0}

  /* back cover */
  .doctor-photo{position:absolute;left:50px;top:290px;width:220px;height:230px;background:linear-gradient(160deg,#e8e6e2,#9aa0a8 60%,#3f4450);border:4px solid var(--paper)}
  .bio{position:absolute;left:300px;top:280px;width:400px;color:#fff;font-family:"Merriweather",Georgia,serif}
  .bio__name{font-family:"Lato",Arial,sans-serif;font-weight:900;font-size:22px;margin-bottom:12px}
  .bio p{font-size:12.5px;line-height:1.55;margin-bottom:12px;text-align:justify}
  .contact{position:absolute;left:50px;top:690px;width:380px;font-size:15px}
  .contact__row{display:flex;align-items:flex-start;gap:14px;margin-bottom:18px;font-weight:700}
  .contact__row svg{flex:none;width:18px;height:18px;fill:var(--purple)}
  .contact__label{color:var(--purple);display:block}
  .contact__note{font-weight:700;display:block}
  .hours{position:absolute;left:470px;top:690px;padding-left:18px;border-left:3px solid var(--purple);font-size:15px;font-weight:700;line-height:1.9}
  .hours__note{color:var(--purple);font-weight:400;font-size:13px}

  /* front cover */
  .brand{position:absolute;right:70px;top:55px;display:flex;align-items:center;gap:14px;font-size:54px;font-weight:700;color:var(--purple);letter-spacing:.5px}
  .brand__dot{width:18px;height:18px;background:var(--purple);border-radius:50%}
  .tagline{position:absolute;left:40px;top:555px;font-size:50px;font-weight:900;line-height:1.15}
  .tagline .accent{color:var(--purple)}
  .tagline .soft{color:var(--grey);font-weight:700}
  .services{position:absolute;left:360px;top:740px;display:grid;grid-template-columns:240px 240px;column-gap:30px;row-gap:26px;font-size:19px;font-weight:700}
  .services li{list-style:none;position:relative;padding-left:22px}
  .services li::before{content:"";position:absolute;left:0;top:8px;width:8px;height:8px;border-radius:50%;background:var(--purple)}
</style>
</head>
<body>

<section class="panel panel--back" aria-label="Folder back cover">
  <svg class="shapes" viewBox="0 0 860 1150" aria-hidden="true">
    <polygon points="0,250 700,250 790,560 0,560" fill="var(--purple)"/>
  </svg>
  <div class="doctor-photo" role="img" aria-label="Portrait photo of the principal dentist"></div>
  <div class="bio">
    <h2 class="bio__name">Dr Leo Brandt</h2>
    <p>Dr Leo Brandt was born in 1972 and raised in England, he graduated from Ashford College, University of Kentmere in 1995. He gained further qualifications in the USA and then worked in general practice in England. He became the Principal Dental Surgeon of The Elmcrest Dental Clinic, UK in 1999. He successfully ran this busy three dentist practice for 9 years, gaining vast experience in general dentistry.</p>
    <p>Dr Leo has advanced training in Intravenous Sedation, Cosmetic Dentistry, Implants, Bone grafting, Sinus lifts, Oral Surgery and Alignora. All of these multi-skills enable him to look after and be solely responsible for his patients.</p>
  </div>

  <div class="contact">
    <div class="contact__row">
      <svg viewBox="0 0 24 24"><path d="M12 2a7 7 0 0 0-7 7c0 5 7 13 7 13s7-8 7-13a7 7 0 0 0-7-7zm0 9.5A2.5 2.5 0 1 1 12 6.5a2.5 2.5 0 0 1 0 5z"/></svg>
      <span>27 Harbour Rd, Westbay, VIC, 3999.<span class="contact__note">(Car Park and Reception Entry via Rear Lane)</span></span>
    </div>
    <div class="contact__row">
      <svg viewBox="0 0 24 24"><path d="M6.6 10.8a15 15 0 0 0 6.6 6.6l2.2-2.2a1 1 0 0 1 1-.25 11.4 11.4 0 0 0 3.6.57 1 1 0 0 1 1 1V20a1 1 0 0 1-1 1A17 17 0 0 1 3 4a1 1 0 0 1 1-1h3.5a1 1 0 0 1 1 1c0 1.25.2 2.45.57 3.57a1 1 0 0 1-.25 1z"/></svg>
      <span>03 9000 4127</span>
    </div>
    <div class="contact__row">
      <svg viewBox="0 0 24 24"><path d="M3 5h18v14H3zm2 2v.5l7 4.5 7-4.5V7z"/></svg>
      <span>info@corveldental-example.com.au</span>
    </div>
    <div class="contact__row">
      <svg viewBox="0 0 24 24"><circle cx="12" cy="12" r="10"/></svg>
      <span>www.corveldental-example.com.au</span>
    </div>
    <div class="contact__row">
      <svg viewBox="0 0 24 24"><path d="M4 4h16v16H4z"/></svg>
      <span><span class="contact__label">Areas We Service:</span>All of Victoria, Bayside, Sandringham, Brighton, Hampton, Bentleigh.</span>
    </div>
  </div>

  <div class="hours">
    <div>Monday 9:00am – 5:00pm</div>
    <div>Tuesday 9:00am – 7:00pm</div>
    <div>*Wednesday 9:00am – 1:00pm</div>
    <div>Thursday 8:00am – 5:00pm</div>
    <div>Friday 7:30am – 2:00pm</div>
    <div class="hours__note">*Administration Only</div>
  </div>
</section>

<section class="panel panel--front" aria-label="Folder front cover">
  <svg class="shapes" viewBox="0 0 860 1150" aria-hidden="true">
    <defs>
      <linearGradient id="photoTone" x1="0" y1="0" x2="1" y2="1">
        <stop offset="0" stop-color="var(--photo-a)"/>
        <stop offset="1" stop-color="var(--photo-b)"/>
      </linearGradient>
    </defs>
    <polygon points="0,195 300,195 430,520 0,520" fill="var(--purple)"/>
    <polygon points="390,690 860,690 860,1150 200,1150" fill="var(--grey-light)"/>
  </svg>
  <svg class="shapes" viewBox="0 0 860 1150" role="img" aria-label="Photo of the dentist consulting a patient in the clinic">
    <polygon points="320,145 860,145 860,640 520,640" fill="url(#photoTone)"/>
  </svg>

  <div class="brand"><span class="brand__dot"></span><span>Corvel Dental</span></div>

  <h1 class="tagline">
    <span class="accent">Your</span> <span class="soft">Smile</span><br>
    <span class="soft">Our</span> <span class="accent">Passion</span>
  </h1>

  <ul class="services">
    <li>Happy Gas</li>
    <li>Alignora</li>
    <li>Oral Surgery</li>
    <li>Teeth Whitening</li>
    <li>Sleep Dentistry</li>
    <li>General Dentistry</li>
    <li>Dental Implants</li>
    <li>Childrens Dentistry</li>
    <li>Cosmetic Dentistry</li>
  </ul>
</section>

</body>
</html>
```